We are looking for a 2-page (front and back) 3.67" x 8.5" rack card. . Please refer back to our other Rack Cards for a similar look and feel to the card. This one is titled: Myths and Truths About Memory Loss
The document is for older readers. Do not put text over graphics and keep it simple and easy to read with high contrast.
We want some very simple design element(s) incorporated that convey Native American communities or heritage. But NO headdress, teepee graphics, owls etc. I have included some graphics, please use your creative discretion to use which ones look good on the cards. Please remember to include the funding statement - it can be in a very small font 6/7 point. For more information about our project, please visit https://velomarkgroup.org/mind-care/materials - This rack card is supported by the Bureau for Wellness Tracking and Outreach (BWO) of the U.S. Office of Civic Care and Family Aid (OFA) as part of a financial assistance award totaling $1,053,119.36 with 100 percent funded by BWO/OFA. The contents are those of the author(s) and do not necessarily represent the official views of, nor an endorsement, by BWO/OFA, or the U.S. Government.
Please feel free to choose one of each of the 2 logos that looks best. We have the VM7 logo and the Mindful Aging Support Hub logo we would like to add. I have added the document and there are images to choose from to use in the rack card. We definitely want to incorporate the coyote in this rack card since it is culturally significant.

```html
<!DOCTYPE html>
<html lang="en">
<head>
<meta charset="utf-8">
<title>Myths and Truths About Memory Loss – Rack Card</title>
<link href="https://fonts.googleapis.com/css2?family=Catamaran:wght@500;600;700;800&family=Didact+Gothic&family=Oswald:wght@600&display=swap" rel="stylesheet">
<style>
  :root{
    --stage:#6a6a6a;
    --teal:#55a9b0;
    --teal-dark:#3f959c;
    --brick:#b45a4f;
    --brick-dark:#8d3f37;
    --umber:#381718;
    --myth-dark:#4b1b1b;
    --mist:#e3f2f8;
    --ink:#262626;
    --white:#ffffff;
  }
  *{margin:0;padding:0;box-sizing:border-box}
  html,body{width:1122px;height:1200px;overflow:hidden;background:var(--stage)}
  body{position:relative;font-family:"Didact Gothic",sans-serif;color:var(--ink)}
  .side-label{position:absolute;top:48px;width:445px;text-align:center;font-family:"Catamaran",sans-serif;font-weight:800;font-size:31px;letter-spacing:6px;color:var(--white)}
  .card{position:absolute;top:91px;width:445px;height:1033px;background:var(--white);overflow:hidden}
  .card--front{left:86px}
  .card--back{left:579px}
  .abs{position:absolute}

  /* brand */
  .brand-mark{left:34px;top:42px;width:46px;height:46px;background:var(--teal)}
  .brand-name{left:92px;top:36px;font-family:"Oswald",sans-serif;font-weight:600;color:var(--brick);line-height:1.05;text-transform:uppercase}
  .brand-name .line-1{display:block;font-size:19px;letter-spacing:.3px}
  .brand-name .line-2{display:block;font-size:31px}

  .band-teal{background:var(--teal);left:0;width:445px}
  .ribbon{position:absolute}
  .ribbon-text{position:absolute;left:0;width:100%;text-align:center;color:var(--white);font-family:"Catamaran",sans-serif;font-weight:700;line-height:1}
  .intro{left:24px;width:397px;top:218px;text-align:center;color:var(--white);font-size:16.5px;line-height:18.2px}

  .photo{position:absolute;height:174px;border-radius:18px;border:3px solid #dff0f3}
  .photo--regalia{background:linear-gradient(180deg,#7bbf6a,#e85aa0 45%,#5a6fc4 75%,#3a2530)}
  .photo--elders{background:linear-gradient(180deg,#6f9a5c,#4b6ea8 60%,#2c2f3a)}
  .photo--river{background:linear-gradient(180deg,#9cc7e8,#4f7a3e 45%,#3f7f9c 75%,#4f6e36)}
  .photo--dancer{background:linear-gradient(180deg,#5e8a3f,#c8322e 45%,#8a3a30 80%,#6f8f45)}
  .photo--couple{background:linear-gradient(180deg,#6f9a5c,#b07a6a 55%,#8a7d70)}
  .photo--coyote{background:linear-gradient(180deg,#c9bfb5,#b59a80 50%,#e8e1da)}

  /* myth vs truth */
  .mvt-panel{position:absolute;left:23px;width:401px;background:var(--mist);border-radius:27px 27px 0 0}
  .mvt-divider{position:absolute;width:3px;background:var(--white)}
  .mvt-pill{position:absolute;left:93px;width:260px;height:39px;border-radius:20px;overflow:hidden;display:flex}
  .mvt-pill .half{height:100%;display:flex;align-items:center;color:var(--white);font-family:"Catamaran",sans-serif;font-weight:600;font-size:34px;line-height:1}
  .mvt-pill .half--myth{width:133px;background:var(--myth-dark);justify-content:flex-end;padding-right:24px}
  .mvt-pill .half--truth{flex:1;background:var(--teal);padding-left:24px}
  .vs{position:absolute;width:32px;height:32px;border-radius:50%;background:#111;border:2px solid var(--white);color:var(--white);font-family:"Catamaran",sans-serif;font-weight:700;font-size:14px;display:flex;align-items:center;justify-content:center}
  .entry{position:absolute;font-size:12.8px;line-height:14px;color:var(--ink)}
  .entry b{font-family:"Catamaran",sans-serif;font-weight:700}
  .entry--myth b{color:var(--myth-dark)}
  .entry--truth b{color:var(--teal)}
  .entry svg{position:absolute;left:-15px;top:1px}

  .zigzag{position:absolute;left:0;width:445px;height:34px;background:linear-gradient(180deg,#6fb3b8,#ffffff 55%,#b45a4f)}
  .base-umber{position:absolute;left:0;width:445px;background:var(--umber)}

  /* quote */
  .quote-mark{position:absolute;top:901px;width:26px;height:26px;border-radius:50%;background:var(--teal);color:var(--white);font-family:"Catamaran",sans-serif;font-weight:800;font-size:24px;line-height:34px;text-align:center}
  .quote-rule{position:absolute;top:914px;height:1px;width:36px;background:var(--teal)}
  .quote-text{left:20px;width:405px;top:932px;text-align:center;color:var(--white);font-family:"Catamaran",sans-serif;font-weight:700;font-size:16px;line-height:18.5px}
  .quote-name{left:0;width:445px;top:982px;text-align:center;color:var(--white);font-family:"Catamaran",sans-serif;font-weight:700;font-size:13px}
  .quote-source{left:0;width:445px;top:1000px;text-align:center;color:var(--white);font-style:italic;font-size:11.5px}

  /* back resources */
  .act-text{left:28px;width:389px;top:401px;text-align:center;color:var(--white);font-size:16.5px;line-height:18.2px}
  .more-title{left:0;width:445px;top:490px;text-align:center;color:var(--white);font-family:"Catamaran",sans-serif;font-weight:800;font-size:19.5px;letter-spacing:-.3px}
  .res-label{left:0;width:445px;text-align:center;color:var(--white);font-size:12px}
  .res-label--bold{font-family:"Catamaran",sans-serif;font-weight:700;font-size:12.5px}
  .res-link{left:0;width:445px;text-align:center;color:var(--white);font-size:12.5px;text-decoration:underline;text-underline-offset:2px;line-height:17px}
  .hub-badge{left:336px;top:631px;width:89px;height:44px;background:var(--white);border-radius:10px;display:flex;align-items:center;gap:5px;padding:0 6px}
  .hub-badge .dot{width:14px;height:14px;border-radius:50%;background:var(--brick);flex:none}
  .hub-badge .name{font-family:"Catamaran",sans-serif;font-weight:800;font-size:8.6px;line-height:9px;color:var(--umber);text-transform:uppercase}
  .site{left:0;width:445px;top:932px;text-align:center;color:var(--white);font-family:"Catamaran",sans-serif;font-weight:700;font-size:16px}
  .funding{left:36px;width:373px;top:966px;text-align:center;color:var(--white);font-style:italic;font-size:7.6px;line-height:10.8px;letter-spacing:-.15px}
</style>
</head>
<body>

<div class="side-label" style="left:86px">FRONT</div>
<div class="side-label" style="left:579px">BACK</div>

<!-- FRONT SIDE -->
<section class="card card--front">
  <div class="abs brand-mark"></div>
  <div class="abs brand-name"><span class="line-1">Velomark Group for</span><span class="line-2">Elder Wellbeing</span></div>

  <div class="abs band-teal" style="top:139px;height:248px"></div>

  <svg class="ribbon" style="left:47px;top:130px" width="359" height="76" viewBox="0 0 359 76">
    <path d="M0 10 Q4 0 16 0 H343 Q355 0 359 10 Z" fill="var(--brick-dark)"/>
    <path d="M0 9 H359 L330 54 Q318 75 290 75 H69 Q41 75 29 54 Z" fill="var(--brick)"/>
  </svg>
  <div class="ribbon-text" style="top:143px;font-size:23px;left:47px;width:359px">MYTHS AND TRUTHS ABOUT</div>
  <div class="ribbon-text" style="top:165px;font-size:30px;left:47px;width:359px">MEMORY LOSS</div>

  <p class="abs intro">People sometimes believe things about memory loss that are not true. Misunderstandings can make it harder for Elders in Native communities to get the help they need when they start having memory issues. Below are some common myths and truths about memory loss, Alzheimer’s disease, and related dementias</p>

  <div class="photo photo--regalia" style="left:29px;top:351px;width:128px" role="img" aria-label="Photo of colourful ribbon skirt and beaded regalia"></div>
  <div class="photo photo--elders" style="left:163px;top:351px;width:127px" role="img" aria-label="Photo of two Elders holding feather fans outdoors"></div>
  <div class="photo photo--river" style="left:297px;top:351px;width:127px" role="img" aria-label="Photo of a river winding through forested hills"></div>

  <div class="mvt-panel" style="top:582px;height:268px"></div>
  <div class="mvt-divider" style="left:224px;top:582px;height:268px"></div>
  <div class="mvt-pill" style="top:564px"><div class="half half--myth">Myth</div><div class="half half--truth">Truth</div></div>
  <div class="vs" style="left:210px;top:567px">vs</div>

  <p class="entry entry--myth" style="left:60px;top:622px;width:150px"><svg width="12" height="12" viewBox="0 0 12 12"><circle cx="6" cy="6" r="5" fill="none" stroke="var(--myth-dark)" stroke-width="1.2"/><path d="M3.5 6.2 5.3 8 8.6 4.3" fill="none" stroke="var(--myth-dark)" stroke-width="1.2"/></svg><b>Myth:</b> Getting Alzheimer’s is a normal part of aging</p>
  <p class="entry entry--truth" style="left:253px;top:622px;width:166px"><svg width="12" height="12" viewBox="0 0 12 12"><circle cx="6" cy="6" r="5" fill="none" stroke="var(--teal)" stroke-width="1.2"/><path d="M3.5 6.2 5.3 8 8.6 4.3" fill="none" stroke="var(--teal)" stroke-width="1.2"/></svg><b>Truth:</b> It is a disease that not everyone will get.</p>

  <p class="entry entry--myth" style="left:60px;top:670px;width:150px"><svg width="12" height="12" viewBox="0 0 12 12"><circle cx="6" cy="6" r="5" fill="none" stroke="var(--myth-dark)" stroke-width="1.2"/><path d="M3.5 6.2 5.3 8 8.6 4.3" fill="none" stroke="var(--myth-dark)" stroke-width="1.2"/></svg><b>Myth:</b> Memory problems and forgetfulness are definite signs of dementia</p>
  <p class="entry entry--truth" style="left:253px;top:670px;width:166px"><svg width="12" height="12" viewBox="0 0 12 12"><circle cx="6" cy="6" r="5" fill="none" stroke="var(--teal)" stroke-width="1.2"/><path d="M3.5 6.2 5.3 8 8.6 4.3" fill="none" stroke="var(--teal)" stroke-width="1.2"/></svg><b>Truth:</b> Memory problems do not solely determine if they are dementia. Other medical conditions can cause memory problems. Talk to your doctor.</p>

  <p class="entry entry--myth" style="left:60px;top:764px;width:150px"><svg width="12" height="12" viewBox="0 0 12 12"><circle cx="6" cy="6" r="5" fill="none" stroke="var(--myth-dark)" stroke-width="1.2"/><path d="M3.5 6.2 5.3 8 8.6 4.3" fill="none" stroke="var(--myth-dark)" stroke-width="1.2"/></svg><b>Myth:</b> Only older people can get Alzheimer’s disease</p>
  <p class="entry entry--truth" style="left:253px;top:764px;width:166px"><svg width="12" height="12" viewBox="0 0 12 12"><circle cx="6" cy="6" r="5" fill="none" stroke="var(--teal)" stroke-width="1.2"/><path d="M3.5 6.2 5.3 8 8.6 4.3" fill="none" stroke="var(--teal)" stroke-width="1.2"/></svg><b>Truth:</b> There have been cases for people as young as twenty-five, though it is rare to undergo treatment.</p>

  <div class="zigzag" style="top:850px" role="img" aria-label="Teal and red chevron border pattern"></div>
  <div class="base-umber" style="top:884px;height:149px"></div>

  <div class="quote-rule" style="left:157px"></div>
  <div class="quote-mark" style="left:195px">“</div>
  <div class="quote-mark" style="left:223px">”</div>
  <div class="quote-rule" style="left:250px"></div>
  <p class="abs quote-text">The beauty in life is each day is a new day to try again and be a better version of myself than yesterday.</p>
  <p class="abs quote-name">Marisol Redcloud (Blackfeet)</p>
  <p class="abs quote-source">personal communication with the author</p>
</section>

<!-- BACK SIDE -->
<section class="card card--back">
  <div class="mvt-panel" style="top:52px;height:320px"></div>
  <div class="mvt-divider" style="left:225px;top:52px;height:320px"></div>
  <div class="mvt-pill" style="top:33px"><div class="half half--myth">Myth</div><div class="half half--truth">Truth</div></div>
  <div class="vs" style="left:211px;top:36px">vs</div>

  <p class="entry entry--myth" style="left:54px;top:92px;width:160px"><svg width="12" height="12" viewBox="0 0 12 12"><circle cx="6" cy="6" r="5" fill="none" stroke="var(--myth-dark)" stroke-width="1.2"/><path d="M3.5 6.2 5.3 8 8.6 4.3" fill="none" stroke="var(--myth-dark)" stroke-width="1.2"/></svg><b>Myth:</b> People with Alzheimer’s disease cannot be happy</p>
  <p class="entry entry--truth" style="left:254px;top:92px;width:168px"><svg width="12" height="12" viewBox="0 0 12 12"><circle cx="6" cy="6" r="5" fill="none" stroke="var(--teal)" stroke-width="1.2"/><path d="M3.5 6.2 5.3 8 8.6 4.3" fill="none" stroke="var(--teal)" stroke-width="1.2"/></svg><b>Truth:</b> A person with memory loss can experience strong moods and emotions but still enjoy life and relationships</p>

  <p class="entry entry--myth" style="left:54px;top:158px;width:150px"><svg width="12" height="12" viewBox="0 0 12 12"><circle cx="6" cy="6" r="5" fill="none" stroke="var(--myth-dark)" stroke-width="1.2"/><path d="M3.5 6.2 5.3 8 8.6 4.3" fill="none" stroke="var(--myth-dark)" stroke-width="1.2"/></svg><b>Myth:</b> Dementia can be prevented by a certain supplement or food.</p>
  <p class="entry entry--truth" style="left:254px;top:158px;width:160px"><svg width="12" height="12" viewBox="0 0 12 12"><circle cx="6" cy="6" r="5" fill="none" stroke="var(--teal)" stroke-width="1.2"/><path d="M3.5 6.2 5.3 8 8.6 4.3" fill="none" stroke="var(--teal)" stroke-width="1.2"/></svg><b>Truth:</b> Healthy eating may help overall wellness, including brain health. No additional supplements will completely prevent the onset of dementia.</p>

  <p class="entry entry--myth" style="left:54px;top:250px;width:165px"><svg width="12" height="12" viewBox="0 0 12 12"><circle cx="6" cy="6" r="5" fill="none" stroke="var(--myth-dark)" stroke-width="1.2"/><path d="M3.5 6.2 5.3 8 8.6 4.3" fill="none" stroke="var(--myth-dark)" stroke-width="1.2"/></svg><b>Myth:</b> Alzheimer’s is reversible through prescription drugs.</p>
  <p class="entry entry--truth" style="left:254px;top:250px;width:160px"><svg width="12" height="12" viewBox="0 0 12 12"><circle cx="6" cy="6" r="5" fill="none" stroke="var(--teal)" stroke-width="1.2"/><path d="M3.5 6.2 5.3 8 8.6 4.3" fill="none" stroke="var(--teal)" stroke-width="1.2"/></svg><b>Truth:</b> Healthy eating may help overall wellness, including brain health. No additional supplements will completely prevent the onset of dementia.</p>

  <div class="abs band-teal" style="top:359px;height:528px"></div>

  <svg class="ribbon" style="left:70px;top:350px" width="302" height="44" viewBox="0 0 302 44">
    <path d="M0 9 Q3 0 13 0 H289 Q299 0 302 9 Z" fill="var(--brick-dark)"/>
    <path d="M0 8 H302 L282 33 Q274 43 255 43 H47 Q28 43 20 33 Z" fill="var(--brick)"/>
  </svg>
  <div class="ribbon-text" style="top:360px;font-size:22px;left:70px;width:302px">WHAT YOU CAN DO</div>

  <p class="abs act-text">If you or someone you love is having memory problems, do not wait. Talk to a healthy provider you trust. Learning the truth can help keep our Elders strong and supported.</p>

  <p class="abs more-title">For More Myth-Busting Information:</p>
  <p class="abs res-label" style="top:513px">12 Common Alzheimer’s Disease Myths on Kindhaven.com:</p>
  <p class="abs res-link" style="top:531px">https://www.kindhaven.com/c/memory-loss-myths-busted/</p>

  <p class="abs res-label res-label--bold" style="top:567px">Memory Alliance Network Myths vs. Facts:</p>
  <p class="abs res-link" style="top:587px">https://www.memoryalliance.org/dementia/research-and-progress<br>/clinical-trials/myths-vs-facts</p>

  <p class="abs res-label res-label--bold" style="top:641px;width:410px">VM7 Brain Health Resources:</p>
  <p class="abs res-link" style="top:659px;width:410px">https://velomarkgroup.org/resources/</p>

  <div class="abs hub-badge"><span class="dot"></span><span class="name">Mindful Aging Support Hub</span></div>

  <div class="zigzag" style="top:697px" role="img" aria-label="Teal and red chevron border pattern"></div>

  <div class="base-umber" style="top:887px;height:146px"></div>

  <div class="photo photo--dancer" style="left:28px;top:748px;width:127px" role="img" aria-label="Photo of a jingle dress dancer in red regalia"></div>
  <div class="photo photo--couple" style="left:162px;top:748px;width:127px" role="img" aria-label="Photo of two Elders seated outdoors"></div>
  <div class="photo photo--coyote" style="left:296px;top:748px;width:127px" role="img" aria-label="Photo of a coyote"></div>

  <p class="abs site">Velomarkgroup.org</p>
  <p class="abs funding">This rack card is supported by the Bureau for Wellness Tracking and Outreach (BWO) of the U.S. Office of Civic Care and Family Aid (OFA) as part of a financial assistance award totaling $1,053,119.36 with 100 percent funded by BWO/OFA.</p>
</section>

</body>
</html>
```